Real Estate "For Sale" Sign for a Colorado Real Estate Company

I need a sign for my Real Estate Company and the size needs to be 24inches by 24inches when printed on metal.
Logo is attached and would like to keep it modern and simple. We are a small town and I am not looking for a new age, industrial design. The concept needs to have the following attributes:

- Logo placed on sign
- Text "For Sale"
- Text "Wade Pellman" and my phone number "720-381-6072" (I would need any font package you use so that I can edit my number if that changes)
- Text "www.wade-pellman.example"
Im open to other attributes as well!

Target Market(s)

General Public driving around town.

Industry/Entity Type

Real Estate Agent

Requirements
Must have
• Logo and the colors must not be too busy. Contact Info very clear.

```html
<!DOCTYPE html>
<html lang="en">
<head>
<meta charset="utf-8">
<title>For Sale Sign – Pine Ridge Realty</title>
<link rel="stylesheet" href="https://fonts.googleapis.com/css2?family=Cinzel:wght@700&family=Libre+Baskerville:wght@700&family=Open+Sans:wght@700&display=swap">
<style>
  :root {
    --brand-navy: #0f3f5e;
    --sale-blue: #0a3d91;
    --band-blue: #063c94;
    --agent-ink: #232323;
    --white: #ffffff;
    --photo-light: #e6e6e6;
    --photo-mid: #cfcfcf;
    --photo-dark: #b4b4b4;
    --rule-dark: #1a1a1a;
    --rule-mid: #6a6a6a;
  }
  html, body {
    margin: 0;
    padding: 0;
    overflow: hidden;
    background: #ffffff;
  }
  .sign {
    position: relative;
    width: 1200px;
    height: 1200px;
    overflow: hidden;
    font-family: "Open Sans", Arial, sans-serif;
  }
  .sign__backdrop {
    position: absolute;
    left: 0; top: 0;
    width: 1200px;
    height: 880px;
    background: linear-gradient(180deg, var(--photo-light) 0%, #dadada 35%, var(--photo-mid) 55%, #e2e2e2 70%, var(--photo-dark) 100%);
  }
  .brand {
    position: absolute;
    left: 0; right: 0;
    top: 230px;
    text-align: center;
    color: var(--brand-navy);
    font-family: "Cinzel", "Times New Roman", serif;
    font-weight: 700;
    line-height: 1;
  }
  .brand__name {
    display: block;
    font-size: 100px;
    letter-spacing: 1px;
  }
  .brand__suffix {
    display: block;
    margin-top: 14px;
    font-size: 44px;
    letter-spacing: 18px;
    padding-left: 18px;
  }
  .headline {
    position: absolute;
    left: 0; right: 0;
    top: 490px;
    margin: 0;
    text-align: center;
    font-family: "Libre Baskerville", "Times New Roman", serif;
    font-weight: 700;
    font-size: 150px;
    line-height: 1;
    color: var(--sale-blue);
    letter-spacing: -2px;
  }
  .agent-name {
    position: absolute;
    left: 0; right: 0;
    top: 755px;
    margin: 0;
    text-align: center;
    font-weight: 700;
    font-size: 74px;
    line-height: 1;
    letter-spacing: 2px;
    color: var(--agent-ink);
    text-transform: uppercase;
  }
  .divider {
    position: absolute;
    left: 0; top: 878px;
    width: 1200px;
    height: 20px;
    background: linear-gradient(90deg, var(--rule-dark) 0%, var(--rule-mid) 50%, var(--rule-dark) 100%);
  }
  .contact {
    position: absolute;
    left: 0; top: 898px;
    width: 1200px;
    height: 302px;
    background: var(--band-blue);
    color: var(--white);
    text-align: center;
  }
  .contact__phone {
    position: absolute;
    left: 0; right: 0;
    top: 22px;
    font-size: 142px;
    line-height: 1.1;
    letter-spacing: 4px;
  }
  .contact__rule {
    position: absolute;
    left: 250px;
    top: 178px;
    width: 700px;
    height: 3px;
    background: var(--white);
  }
  .contact__web {
    position: absolute;
    left: 0; right: 0;
    top: 216px;
    font-size: 44px;
    line-height: 1.1;
  }
</style>
</head>
<body>
  <main class="sign">
    <div class="sign__backdrop" role="img" aria-label="Faded grey photograph of a suburban house with a driveway, lawn and sidewalk"></div>

    <div class="brand">
      <span class="brand__name">Pine Ridge Realty</span>
      <span class="brand__suffix">LLC</span>
    </div>

    <h1 class="headline">FOR SALE</h1>

    <p class="agent-name">Wade Pellman</p>

    <div class="divider"></div>

    <section class="contact">
      <div class="contact__phone">720-381-6072</div>
      <div class="contact__rule"></div>
      <div class="contact__web">www.wade-pellman.example</div>
    </section>
  </main>
</body>
</html>
```